Indian Takeaway Menu

We need a flyer for an existing Indian Takeaway business in dublin Ireland.

We need some upto date style menu may be a A4 sheet folded in 3 layers.

But not folded in landscape side folded from portrait side and typing from portrait side from top, as we type in a word document and then fold the letter in 3 layers.
please amend your designs as everyone have done the same thing which is very boring.

We have a logo we would like to use in front of the menu. Designer have to come up with the colour which will help the logo to stand out. we also have a review in the paper which we would like to use at the back page somewhere.

New ideas are welcome from the designer
Please look at the example menu attached.

City population

Landscape

Font styles to use
Sans Serif

Colors
acd037

Requirements
Must have
• ingredient sign for
• Nuts
• Celiac
• Low fat
• Diary
Nice to have
• attractive

```html
<!DOCTYPE html>
<html lang="en">
<head>
<meta charset="utf-8">
<title>Takeaway Menu – Inside Spread</title>
<link href="https://fonts.googleapis.com/css2?family=Arimo:wght@400;700&display=swap" rel="stylesheet">
<style>
  :root {
    --lime: #adf22c;
    --ink: #111111;
    --paper: #ffffff;
    --chilli: #d8261a;
    --chilli-stem: #3d8a1e;
    --badge: #111111;
    --badge-text: #adf22c;
  }
  * { margin: 0; padding: 0; box-sizing: border-box; }
  html, body { width: 1200px; height: 850px; overflow: hidden; background: var(--paper); }
  body { font-family: "Arimo", Arial, sans-serif; color: var(--ink); }

  .spread { position: relative; width: 1200px; height: 850px; background: var(--paper); }

  .panel {
    position: absolute; top: 28px; height: 782px;
    background: var(--lime);
    border: 4px double var(--ink);
    border-radius: 16px;
  }
  .panel--left { left: 22px; width: 360px; }
  .panel--middle { left: 418px; width: 358px; }
  .panel--right { left: 813px; width: 368px; }

  .section-title { position: absolute; left: 0; right: 0; font-size: 13px; font-weight: 700; line-height: 16px; text-align: center; }

  /* Dish list */
  .dish { position: absolute; left: 16px; width: 318px; }
  .dish__name { font-size: 11px; font-weight: 700; line-height: 13px; white-space: nowrap; overflow: hidden; width: 238px; }
  .dish__price { position: absolute; top: 0; left: 242px; font-size: 11px; font-weight: 700; line-height: 13px; }
  .dish__desc { font-size: 7.6px; line-height: 10px; margin-top: 1px; width: 310px; }
  .chilli { position: absolute; top: -4px; left: 222px; width: 20px; height: 16px; }

  /* Allergen key */
  .allergen-key { position: absolute; left: 16px; top: 748px; display: flex; gap: 10px; font-size: 7.6px; line-height: 12px; }
  .allergen-key__item { display: flex; align-items: center; gap: 3px; }
  .allergen-key__badge {
    display: inline-block; min-width: 12px; height: 12px; padding: 0 2px; border-radius: 6px;
    background: var(--badge); color: var(--badge-text); font-weight: 700; font-size: 6.5px; line-height: 12px; text-align: center;
  }

  /* Meal deals */
  .deal { position: absolute; left: 18px; width: 320px; }
  .deal__name { font-size: 11px; font-weight: 700; line-height: 13px; white-space: nowrap; overflow: hidden; width: 250px; }
  .deal__price { position: absolute; top: 0; left: 257px; font-size: 11px; font-weight: 700; line-height: 13px; }
  .deal__items { list-style: none; padding-left: 50px; font-size: 11px; line-height: 13px; }
  .deal__items .gap { margin-top: 3px; }

  .photo { position: absolute; border-radius: 12px; }
  .photo--thali {
    left: 30px; top: 612px; width: 285px; height: 153px;
    background: radial-gradient(ellipse at 45% 50%, #f4f2ea 0 22%, #8e8a82 40%, #c6a35a 60%, #5a4c3c 100%);
  }

  /* Sides */
  .price-list { position: absolute; left: 17px; top: 61px; width: 320px; }
  .price-row { position: relative; height: 19.3px; }
  .price-row__label { display: block; font-size: 11px; line-height: 19px; white-space: nowrap; overflow: hidden; width: 246px; }
  .price-row__label--sub { padding-left: 16px; }
  .price-row__amount { position: absolute; top: 0; left: 256px; font-size: 11px; line-height: 19px; }

  .kids { position: absolute; left: 45px; top: 477px; width: 270px; }
  .kids__row { position: relative; height: 25.3px; font-size: 11px; font-weight: 700; line-height: 14px; white-space: nowrap; }
  .kids__label { display: block; width: 221px; overflow: hidden; }
  .kids__amount { position: absolute; top: 0; left: 221px; }

  .photo-strip { position: absolute; left: 14px; top: 572px; width: 321px; height: 196px; display: flex; gap: 2px; }
  .photo-strip div { flex: 1; }
  .photo-strip .paneer { background: linear-gradient(160deg, #c0631e, #e3a24c 55%, #f4e3b8); }
  .photo-strip .biryani { background: linear-gradient(170deg, #8a5428, #c99856 50%, #efe8d8); }
  .photo-strip .aloo { background: linear-gradient(170deg, #5f7a2a, #d6b44a 50%, #a98236); }
  .photo-strip .tandoori { background: linear-gradient(170deg, #a8281c, #e0583a 55%, #c53a24); }
</style>
</head>
<body>
<main class="spread">

  <svg width="0" height="0" style="position:absolute">
    <symbol id="chilli-mark" viewBox="0 0 20 16"><path d="M2 14 C8 14 14 10 16 4 L18 5 C16 12 9 16 2 14 Z" fill="var(--chilli)"/><path d="M16 4 L19 1" stroke="var(--chilli-stem)" stroke-width="2"/></symbol>
  </svg>

  <section class="panel panel--left">
    <div class="dish" style="top:44px"><p class="dish__name">29.Tandoori Prawn Masala (Mild) ...........................................</p><span class="dish__price">€10.00</span>
      <p class="dish__desc">Sauteed prawns in a smooth creamy sauce flavoured with kasoori methi &amp; tandoori spices</p></div>
    <div class="dish" style="top:88px"><p class="dish__name">30.Prawn Karahi...........................................................</p>
      <svg class="chilli" role="img" aria-label="Hot chilli marker"><use href="#chilli-mark"/></svg><span class="dish__price">€10.00</span>
      <p class="dish__desc">Succulent prawns cooked with green peppers, spring onion, tomatoes &amp; whole spices</p></div>
    <div class="dish" style="top:134px"><p class="dish__name">31.Goan Prawn Curry ...................................................</p>
      <svg class="chilli" role="img" aria-label="Hot chilli marker"><use href="#chilli-mark"/></svg><span class="dish__price">€10.50</span>
      <p class="dish__desc">Fisherman's favourite prawn curry flavoured with curry leaves, coconut, crushed spices &amp; fresh herbs</p></div>
    <div class="dish" style="top:181px"><p class="dish__name">32.Prawn Biryani................</p>
      <svg class="chilli" role="img" aria-label="Hot chilli marker"><use href="#chilli-mark"/></svg><span class="dish__price">€10.00</span>
      <p class="dish__desc">Shrimp prawn cooked with egg, green peas &amp; onion</p></div>
    <div class="dish" style="top:213px"><p class="dish__name">33. Chicken Dupiaza ..........</p><span class="dish__price">€8.00</span>
      <p class="dish__desc">Chicken breast pieces cooked with fresh tomato &amp; sliced onions</p></div>
    <div class="dish" style="top:246px"><p class="dish__name">34. Chicken Rogan Josh..............</p><span class="dish__price">€8.00</span>
      <p class="dish__desc">A red chicken curry prepared with fresh herb &amp; spices, a delicacy from Kashmir</p></div>
    <div class="dish" style="top:282px"><p class="dish__name">35. Chicken Madras ...................</p><span class="dish__price">€8.00</span>
      <p class="dish__desc">Chicken cooked in a hot spicy sauce</p></div>
    <div class="dish" style="top:317px"><p class="dish__name">36. Tarkari Makhani .....</p><span class="dish__price">€8.00</span>
      <p class="dish__desc">Mixed seasonal vegetables in a smooth butter, cream &amp; tomato sauce</p></div>

    <h2 class="section-title" style="top:358px">Vegetarian Dishes</h2>

    <div class="dish" style="top:387px"><p class="dish__name">37.Gajar Mater Paneer............................................</p>
      <svg class="chilli" role="img" aria-label="Hot chilli marker"><use href="#chilli-mark"/></svg><span class="dish__price">€8.00</span>
      <p class="dish__desc">Mild. A colourful combination of chopped carrots, peas &amp; Indian cheese in semi-dry sauce - chef's special for vegetarians (recommended)</p></div>
    <div class="dish" style="top:435px"><p class="dish__name">38.Dhingri Dulma ...............................................</p>
      <svg class="chilli" role="img" aria-label="Hot chilli marker"><use href="#chilli-mark"/></svg><span class="dish__price">€10.50</span>
      <p class="dish__desc">Mild. Fresh mushroom &amp; Indian cheese fried with onion, ginger &amp; garlic in mild spices</p></div>
    <div class="dish" style="top:483px"><p class="dish__name">39.Dum Wale Aloo ....................................................</p><span class="dish__price">€7.70</span>
      <p class="dish__desc">Potatoes cooked with fresh ginger, garlic, onions, tomatoes curry leaves &amp; slow cooked with cumin flavoured yoghurt</p></div>
    <div class="dish" style="top:526px"><p class="dish__name">40.Karahi Paneer ....................................................</p><span class="dish__price">€7.70</span>
      <p class="dish__desc">A Semi-dry and colourful curry is prepared using homemade Indian cheese (paneer)</p></div>
    <div class="dish" style="top:573px"><p class="dish__name">41.Paneer Jalferzi ....................................................</p><span class="dish__price">€8.00</span>
      <p class="dish__desc">Stir fried homemade cottage cheese &amp; peppers with roasted coriander seeds, fresh tomato, onion &amp; green chillies.</p></div>
    <div class="dish" style="top:617px"><p class="dish__name">42.Sambhar Vegetable Curry ...........................................</p><span class="dish__price">€7.70</span>
      <p class="dish__desc">Mixed seasonal vegetable curry cooked with little lentil, coconut, curry leaves, mustard &amp; fresh coriander (recommended)</p></div>
    <div class="dish" style="top:661px"><p class="dish__name">43.Aloo Saag Haryali ...................................................</p><span class="dish__price">€7.70</span>
      <p class="dish__desc">Pan fried potatoes &amp; spinach, flavoured with kasoori methi &amp; fresh coriander</p></div>
    <div class="dish" style="top:695px"><p class="dish__name">44.Vegetable Biryani Orraita..............</p><span class="dish__price">€8.50</span>
      <p class="dish__desc">Basmati Rice cooked with mixed seasonal vegetables, fresh herbs, spices &amp; fried golden onion. Served with your choice of mixed vegetable</p></div>

    <ul class="allergen-key" aria-label="Allergen signs">
      <li class="allergen-key__item"><span class="allergen-key__badge">N</span>Nuts</li>
      <li class="allergen-key__item"><span class="allergen-key__badge">C</span>Celiac</li>
      <li class="allergen-key__item"><span class="allergen-key__badge">LF</span>Low fat</li>
      <li class="allergen-key__item"><span class="allergen-key__badge">D</span>Dairy</li>
    </ul>
  </section>

  <section class="panel panel--middle">
    <h2 class="section-title" style="top:41px">Meal Deal</h2>
    <div class="deal" style="top:74px"><p class="deal__name">Set Meal A For 1 (Vegetarian)...................................</p><span class="deal__price">€14.00</span>
      <ul class="deal__items"><li>Gole bhajia</li><li class="gap">Sambhar vegetable curry</li><li class="gap">Pilau rice</li><li>Naan</li><li class="gap">Poppadoms &amp; spiced onion</li><li>Soft Drink</li></ul></div>
    <div class="deal" style="top:188px"><p class="deal__name">Set Meal B For 1 (Non Vegetarian).......... .</p><span class="deal__price">€16.00</span>
      <ul class="deal__items"><li>Chicken tikka</li><li class="gap">Chicken tikka masala</li><li class="gap">Pilau rice</li><li>Naan</li><li class="gap">Poppadom &amp; spiced onion</li><li>Soft Drink</li></ul></div>
    <div class="deal" style="top:303px"><p class="deal__name">Set Meal For 2...............................................</p><span class="deal__price">€25.00</span>
      <ul class="deal__items"><li>Gole bhajia</li><li class="gap">Chicken tikka</li><li class="gap">Chicken tikka masala</li><li class="gap">Lamb Roganjosh</li><li class="gap">Pilau rice</li><li>naan</li><li class="gap">Poppadom &amp; spiced onion</li><li>2 Soft Drinks</li></ul></div>
    <div class="deal" style="top:452px"><p class="deal__name">Set Meal for 3/4..................................................</p><span class="deal__price">€39.00</span>
      <ul class="deal__items"><li>Gole bhajia</li><li class="gap">Vegetable samosa</li><li class="gap">Chicken tikka</li><li class="gap">Chicken Tikka Masala</li><li class="gap">Prawn Karahi</li><li class="gap">Sambhar Vegetable</li><li>2 Pilau Rice</li><li class="gap">Poppadom &amp; spiced onion</li><li>2 Soft Drinks</li></ul></div>
    <div class="photo photo--thali" role="img" aria-label="Photo of a thali platter with rice, curries and dips"></div>
  </section>

  <section class="panel panel--right">
    <h2 class="section-title" style="top:41px">Nan Bread &amp; Side Orders</h2>
    <div class="price-list">
      <div class="price-row"><span class="price-row__label">1.Naan.................................................................</span><span class="price-row__amount">€1.90</span></div>
      <div class="price-row"><span class="price-row__label">2.Garlic Naan.................................</span><span class="price-row__amount">€2.50</span></div>
      <div class="price-row"><span class="price-row__label price-row__label--sub">* Garlic Chilli Naan ..............................................</span><span class="price-row__amount">€3.00</span></div>
      <div class="price-row"><span class="price-row__label">3. Peshwari Naan.................................................</span><span class="price-row__amount">€2.70</span></div>
      <div class="price-row"><span class="price-row__label">4. Keema Naan....................................................</span><span class="price-row__amount">€3.00</span></div>
      <div class="price-row"><span class="price-row__label">5.Coriander Naan..................................................</span><span class="price-row__amount">€2.50</span></div>
      <div class="price-row"><span class="price-row__label">6.Blue Cheese Naan...............................</span><span class="price-row__amount">€2.50</span></div>
      <div class="price-row"><span class="price-row__label price-row__label--sub">* G.O.C..........................................................</span><span class="price-row__amount">€3.00</span></div>
      <div class="price-row"><span class="price-row__label">7. Boiled Basmati.........................................</span><span class="price-row__amount">€2.00</span></div>
      <div class="price-row"><span class="price-row__label">8. Pilau Rice.......................................................</span><span class="price-row__amount">€2.10</span></div>
      <div class="price-row"><span class="price-row__label">9.Vegetable &amp; Fruit Pilau..........................................</span><span class="price-row__amount">€2.50</span></div>
      <div class="price-row"><span class="price-row__label">10. Poppodum(2) &amp; Spiced Onion...............................</span><span class="price-row__amount">€2.00</span></div>
      <div class="price-row"><span class="price-row__label">11.Onion,Mint &amp; Cucumber Riata ..............................</span><span class="price-row__amount">€2.00</span></div>
      <div class="price-row"><span class="price-row__label">12. Mix Pickle Dips .........................................</span><span class="price-row__amount">€2.00</span></div>
      <div class="price-row"><span class="price-row__label price-row__label--sub">* Bombay Aloo.................................................</span><span class="price-row__amount">€5.00</span></div>
      <div class="price-row"><span class="price-row__label price-row__label--sub">* Tarka Dal Lentil curry ..........................................</span><span class="price-row__amount">€4.50</span></div>
      <div class="price-row"><span class="price-row__label price-row__label--sub">* Saag Paneer Spinach &amp; Indian chees.........</span><span class="price-row__amount">€5.50</span></div>
      <div class="price-row"><span class="price-row__label price-row__label--sub">* Aloo Ghobi side...............................................</span><span class="price-row__amount">€5.00</span></div>
      <div class="price-row"><span class="price-row__label price-row__label--sub">* Aloo Choley Masala Side.......................................</span><span class="price-row__amount">€5.00</span></div>
    </div>

    <h2 class="section-title" style="top:454px">Kids Meals</h2>
    <div class="kids">
      <div class="kids__row"><span class="kids__label">Kids Chicken Korma with rice...........................................</span><span class="kids__amount">€6.00</span></div>
      <div class="kids__row"><span class="kids__label">Kids Chic Tikka Masala with rice.......................................</span><span class="kids__amount">€6.00</span></div>
      <div class="kids__row"><span class="kids__label">Kids Cheese Tikka Naan...........................................</span><span class="kids__amount">€3.00</span></div>
      <div class="kids__row"><span class="kids__label">Doner Kebab in Nan Bread ...........................................</span><span class="kids__amount">€7.00</span></div>
    </div>

    <div class="photo-strip">
      <div class="paneer" role="img" aria-label="Photo of paneer curry"></div>
      <div class="biryani" role="img" aria-label="Photo of chicken biryani"></div>
      <div class="aloo" role="img" aria-label="Photo of potato curry with coriander"></div>
      <div class="tandoori" role="img" aria-label="Photo of tandoori chicken with lime"></div>
    </div>
  </section>

</main>
</body>
</html>
```